Wager Policy & Public Outlook Network (WPPON) Website
New site required for UK based Group
Wager Policy & Public Outlook Network (WPPON) Website - Information
Creative Brief
Information
http://www.wppon-network.org/
We are a UK based charitable group, aiming to raise awareness of problem gambling. We currently have a very basic website and are looking to have a professional, clean site designed to incorporate our existing material, forum and chatroom.
below header
http://www.lumarex.com
http://www.k9.co.uk
We also have a forum at http://www.wppon-network.org.uk and have chat facilities available through the main site. I will make our logo available for the project as well as the content we would like to see.

```html
<!DOCTYPE html>
<html lang="en">
<head>
<meta charset="utf-8">
<title>WPPON – Society Perception</title>
<link href="https://fonts.googleapis.com/css2?family=Crimson+Text&family=Open+Sans:wght@300;400;600&family=Arimo:ital,wght@0,400;0,700;1,400&display=swap" rel="stylesheet">
<style>
:root{
  --red:#c0272d;
  --ink:#555;
  --muted:#8a8a8a;
  --rule:#d4d4d4;
  --panel:#161616;
  --panel-text:#cfcfcf;
  --white:#fff;
}
*{margin:0;padding:0;box-sizing:border-box}
html,body{width:1200px;height:677px;overflow:hidden;background:var(--white)}
body{position:relative;font-family:"Arimo",Arial,sans-serif;color:var(--ink)}
a{color:inherit;text-decoration:none}

.brand{position:absolute;left:40px;top:30px;font-family:"Open Sans",Arial,sans-serif;font-weight:400;font-size:24px;color:var(--red)}

.main-nav{position:absolute;left:245px;top:66px;display:flex;gap:30px;font-size:11px;color:var(--muted)}
.main-nav .active{color:var(--red)}
.header-rule{position:absolute;left:205px;top:88px;width:735px;height:1px;background:var(--rule)}

.page-title{position:absolute;left:205px;top:136px;font-family:"Crimson Text",Georgia,serif;font-size:38px;line-height:44px;color:var(--red);font-weight:400}

.quote{position:absolute;left:14px;top:196px;width:180px;font-size:8px;line-height:10px;text-align:right;font-style:italic;color:#333}
.quote cite{display:block;font-style:normal;margin-top:3px}

.side-links{position:absolute;left:0;top:288px;width:195px}
.side-links a{display:block;text-align:center;font-family:"Open Sans",Arial,sans-serif;font-size:16px;color:var(--red);padding:10px 0 12px;border-bottom:1px solid var(--rule)}
.side-links a:last-child{border-bottom:none}

.content{position:absolute;left:205px;top:196px;width:730px;font-size:8.4px;line-height:10.6px;color:var(--muted)}
.content p{margin-bottom:11px}
.content .lead{color:var(--red)}

.footer-rule{position:absolute;left:205px;top:598px;width:735px;height:1px;background:var(--rule)}
.footer-nav{position:absolute;left:245px;top:608px;display:flex;gap:30px;font-size:11px;color:var(--muted)}
.footer-nav .active{color:var(--red)}

.sidebar{position:absolute;left:943px;top:0;width:257px;height:677px;background:var(--panel);color:var(--panel-text);font-family:"Open Sans",Arial,sans-serif}
.account{position:absolute;left:42px;top:68px;font-size:10px;color:var(--white)}
.account .sep{color:var(--red);margin:0 5px}
.account .reg{color:var(--red)}
.sidebar h2{position:absolute;left:24px;font-weight:300;color:var(--white)}
.tweets-title{top:92px;font-size:21px}
.tweets{position:absolute;left:24px;top:128px;width:210px;list-style:none}
.tweets li{font-size:6.5px;line-height:8px;color:var(--red);margin-bottom:9px}
.tweets li span{display:block;text-align:right;color:#777;font-size:5.5px}
.tweets li.link{color:#999}
.forum-title{top:412px;font-size:50px}
.forum-text{position:absolute;left:24px;top:482px;width:200px;font-size:6.5px;line-height:8px;color:#999}
.forum-text p{margin-bottom:8px}
.copyright{position:absolute;right:14px;bottom:8px;font-size:6px;color:#888}
</style>
</head>
<body>
<header>
  <a class="brand" href="#">WPPON</a>
  <nav class="main-nav">
    <a href="#">About WPPON</a><a href="#">Reform</a><a class="active" href="#">Society Perception</a><a href="#">Forum</a><a href="#">Chatroom</a><a href="#">Donate</a><a href="#">Contact us</a>
  </nav>
  <div class="header-rule"></div>
</header>

<h1 class="page-title">Society Perception</h1>

<blockquote class="quote">"If we never put a fence at the top of the cliff we will only keep paying for more help at the bottom"<cite>Daniel Marsh MP on problem gambling February 2017</cite></blockquote>

<nav class="side-links">
  <a href="#">Donate</a>
  <a href="#">start chatting</a>
  <a href="#">contact us</a>
</nav>

<main class="content">
  <p class="lead">WELCOME TO THE HOMEPAGE OF THE WAGER POLICY AND PUBLIC OUTLOOK NETWORK (WPPON)! OUR AIM IS TO RAISE AWARENESS OF PROBLEM GAMBLING &amp; RESTRICT THE DAMAGE BEING DONE TO THE YOUNG, VULNERABLE, FAMILY MEMBERS &amp; SOCIETY FROM THIS INSIDIOUS ADDICTION - REGISTER ON THE WPPON FORUM TO BECOME A MEMBER &amp; HELP OUR CAUSE. YOU CAN ALSO FOLLOW US ON TWITTER @thewpponnetwork<br>The Wager Policy &amp; Public Outlook Network (WPPON) was set up in October 2015 to cover five key points:</p>
  <p>Educate society on the dangers of problem gambling, which can be done through the gaming industry itself. The public must be made aware of the potential consequences of gambling, the dangers of problem gaming and the true costs of the people affected with this addiction. WPPON would like to see the government change it's stance, similar to how it did with the tobacco industry.</p>
  <p>Impose safety nets to protect young and vulnerable gamblers albeit online or in person, which again can be done via the gaming industry with co-operation from the banking sector.</p>
  <p>Devote advertising laws on gambling products and initiate public awareness campaigns.</p>
  <p>Education for schools, health authorities and employers etc on the harmful effects of problem gaming.</p>
  <p>A self-exclusion policy to cover every licensed gambling establishment in Great Britain.</p>
  <p>We believe that treatment for compulsive gamblers has improved since 2000, but we're looking to start something that's proactive rather than reactive to this serious addiction.</p>
  <p>With so many ways to gamble in the 21st century, this silent addiction is seducing more and more people who may not understand it's dangers and implications. 21st century gambling is the perfect vehicle for an addict; quick clandestine conditions, they control the speed and duration and no need to leave the establishment.</p>
  <p>WPPON doesn't want gambling banned, it's an enjoyable pastime for 83% of the adult population in Great Britain. However it's potentially extremely addictive, which can lead to take control of people's lives and actions, including their work and lifestyle.</p>
  <p>Under the Wagering Standards Board's licensing code, the licensed betting office must do all it can to protect young and vulnerable people from problem gambling. Whatever you read or hear, we believe that this is simply not being done, as the industry needs addicts to bolster big profits.</p>
</main>

<div class="footer-rule"></div>
<nav class="footer-nav">
  <a href="#">About WPPON</a><a href="#">Reform</a><a class="active" href="#">Society Perception</a><a href="#">Forum</a><a href="#">Chatroom</a><a href="#">Donate</a><a href="#">Contact us</a>
</nav>

<aside class="sidebar">
  <div class="account"><a href="#">log in</a><span class="sep">|</span><a class="reg" href="#">Register</a></div>
  <h2 class="tweets-title">Latest Tweets</h2>
  <ul class="tweets">
    <li>New figures show a rise in online betting among young adults this year<span>About 1 hour ago</span></li>
    <li>Join our forum and share your story with others who understand<span>About 3 hours ago</span></li>
    <li>Council calls for tighter rules on high street betting shops<span>Yesterday</span></li>
    <li>Thank you to all who supported our awareness week<span>2 days ago</span></li>
    <li class="link">http://www.wppon-network.org.uk</li>
  </ul>
  <h2 class="forum-title">Forum</h2>
  <div class="forum-text">
    <p>Feel free to talk about anything and everything gambling related on the board</p>
    <p>Discuss your gambling issues with WPPON forum members</p>
    <p>Ask our members ... but we'll do our best to answer</p>
    <p>http://www.wppon-network.org.uk</p>
  </div>
  <div class="copyright">© Wager Policy &amp; Public Outlook</div>
</aside>
</body>
</html>
```